Flyer for Merchant Capital Cash Advance business

Need Flyer Design to be advertised on Social Media Platforms and also Print it to Publish it in Magazines.
Flyer Will be printed in different sizes for different publications.
Size 1) 6.25 inches * 11 inches.
Size 2) 8 inch * 11 inch
Size 3) 8 inch * 5.5 I inch
Size 4) 5 inch * 7 inch.
Google “Merchant Capital Cash advance flyer pics” to get an idea.

Flyer Design for Merchant Cash advance business.

Merchant Cash Advance is alternate to bank loans and does not require Personal Guarantee or Collateral.
Updates

Need extra days to review

Target Market(s)

Business owners seeking loan.

Industry/Entity Type

Business Service

Font styles to use
Serif
Sans Serif
Decorative
Script

Colors

Designer to choose colors to be used in the design.

Requirements
Must have
• Content from the Files Uploaded.
• Sharp Colors.
Nice to have
• Would like to see flyer in shape of a Bank Check or a $100 Bill.
• Would like to show a Comparison between Bank Loan and MCA.
• Open to any other ideas.

```html
<!DOCTYPE html>
<html lang="en">
<head>
<meta charset="utf-8">
<title>Business Funding Made Easy – Flyer</title>
<link rel="stylesheet" href="https://fonts.googleapis.com/css2?family=Anton&family=Oswald:wght@500;700&family=Cinzel:wght@600;700&display=swap">
<style>
  :root{
    --backdrop:#7a8296;
    --paper:#ffffff;
    --red:#e8173a;
    --blue:#2b4aa6;
    --navy:#262c3d;
    --ink:#111111;
    --money-1:#d9ddd2;
    --money-2:#b9c1b4;
    --check:#1aa34a;
    --cross:#e3141c;
  }
  *{box-sizing:border-box;margin:0;padding:0}
  html,body{width:1200px;height:720px;overflow:hidden;background:var(--backdrop)}
  .flyer{position:absolute;left:374px;top:49px;width:454px;height:623px;background:var(--paper);overflow:hidden}
  .money-backdrop{position:absolute;inset:0 0 130px 0;
    background:
      radial-gradient(ellipse 150px 230px at 50% 45%, #fff 55%, rgba(255,255,255,0) 100%),
      linear-gradient(180deg, rgba(255,255,255,0) 70%, #fff 100%),
      linear-gradient(135deg, var(--money-1), var(--money-2) 40%, var(--money-1) 70%, var(--money-2));}
  .hero-photo{position:absolute;left:0;top:399px;width:266px;height:196px;
    background:linear-gradient(160deg, rgba(255,255,255,0) 0%, #8c93a3 35%, #4a5468 70%, #cfd4dc 100%);
    -webkit-mask:linear-gradient(90deg,#000 70%,transparent);mask:linear-gradient(90deg,#000 70%,transparent)}
  .center{position:absolute;left:0;width:100%;text-align:center;white-space:nowrap}
  .headline{top:18px;font-family:"Anton",sans-serif;font-size:30px;line-height:1;color:var(--red);letter-spacing:-.2px}
  .headline-rule{position:absolute;left:58px;width:338px;top:50px;height:1.5px;background:var(--red)}
  .tagline{top:56px;font-family:"Cinzel",serif;font-weight:600;font-size:14.5px;color:var(--blue);letter-spacing:.5px}
  .product{top:84px;font-family:"Oswald",sans-serif;font-weight:700;font-size:15.5px;color:var(--red);line-height:1.1}
  .product span{border-bottom:1.5px solid var(--red);padding:0 4px 1px}
  .range{top:113px;font-family:"Cinzel",serif;font-weight:700;font-size:15px;color:var(--blue)}
  .benefits{position:absolute;left:0;width:100%;top:141px;text-align:center;list-style:none;font-family:"Cinzel",serif;font-weight:700;font-size:14.5px;line-height:13.4px}
  .benefits li:nth-child(odd){color:var(--red)}
  .benefits li:nth-child(even){color:var(--blue)}
  .apply-banner{position:absolute;left:74px;top:232px;width:305px;height:32px;background:var(--blue);color:#fff;
    font-family:"Oswald",sans-serif;font-weight:700;font-size:22px;line-height:32px;text-align:center}
  .compare-card{position:absolute;left:122px;top:274px;width:208px;height:152px;background:#fff;border:2px solid var(--ink)}
  .compare-title{position:absolute;top:6px;left:0;width:100%;text-align:center;font-family:"Oswald",sans-serif;font-weight:700;font-size:11px;text-decoration:underline;color:var(--ink)}
  .compare-sub{position:absolute;top:32px;left:0;width:100%;text-align:center;font-family:"Cinzel",serif;font-weight:600;font-size:7px;line-height:8px;color:var(--ink)}
  .compare-table{position:absolute;left:4px;top:56px;width:196px;height:88px;border:1px solid #555;border-collapse:collapse;font-family:"Cinzel",serif;font-size:3.6px;color:var(--ink)}
  .compare-table th{font-family:"Oswald",sans-serif;font-weight:700;font-size:3.8px;line-height:4px;border:1px solid #555;height:13px}
  .compare-table td{border:1px solid #555;height:10.5px;text-align:center}
  .compare-table td.label{border:none;text-align:left;padding-left:5px;width:121px;line-height:3.8px}
  .compare-table th.blank{border:none;border-right:1px solid #555}
  .compare-table svg{width:6px;height:6px;vertical-align:middle}
  .contact{position:absolute;right:17px;text-align:right;white-space:nowrap;color:var(--red);font-family:"Cinzel",serif;font-weight:700}
  .company{top:478px;font-size:13px}
  .phone{top:491px;font-size:31px;line-height:1.1}
  .email{top:526px;font-size:11.5px}
  .footer-band{position:absolute;left:0;bottom:0;width:100%;height:28px;background:var(--navy)}
</style>
</head>
<body>
<main class="flyer">
  <div class="money-backdrop" role="img" aria-label="Scattered hundred-dollar bills framing the page"></div>
  <div class="hero-photo" role="img" aria-label="Relaxed businessman leaning back on a sofa"></div>

  <h1 class="center headline">BUSINESS FUNDING MADE EASY</h1>
  <div class="headline-rule"></div>
  <p class="center tagline">A CONVENIENT ALTERNATIVE TO BANK LOAN</p>
  <p class="center product"><span>BUSINESS CAPITAL CASH ADVANCE</span></p>
  <p class="center range">FROM $5K – $1 Mil</p>

  <ul class="benefits">
    <li>Noo Personal Guarantee</li>
    <li>No Collateral</li>
    <li>No Minimum Credit Score</li>
    <li>Bankruptcy OK</li>
    <li>Opportunity to Renew Your Cash Advance</li>
    <li>for Additional Funds</li>
  </ul>

  <div class="apply-banner">Simple One Page Application</div>

  <section class="compare-card">
    <h2 class="compare-title">Business Funding Made Easy</h2>
    <p class="compare-sub">A Convenient Alternative to Bank Loan<br>Business Capital Cash Advance</p>
    <table class="compare-table">
      <tr><th class="blank"></th><th>Business Capital<br>Cash Advance</th><th>Bank Loan</th></tr>
      <tr><td class="label">• No Personal Guarantee</td><td><svg viewBox="0 0 10 10"><path d="M1 5l3 3 5-7" fill="none" stroke="var(--check)" stroke-width="1.8"/></svg></td><td><svg viewBox="0 0 10 10"><path d="M2 2l6 6M8 2l-6 6" stroke="var(--cross)" stroke-width="2.2"/></svg></td></tr>
      <tr><td class="label">• No Collateral or Guarantors</td><td><svg viewBox="0 0 10 10"><path d="M1 5l3 3 5-7" fill="none" stroke="var(--check)" stroke-width="1.8"/></svg></td><td><svg viewBox="0 0 10 10"><path d="M2 2l6 6M8 2l-6 6" stroke="var(--cross)" stroke-width="2.2"/></svg></td></tr>
      <tr><td class="label">• No Minimum Credit Score Required</td><td><svg viewBox="0 0 10 10"><path d="M1 5l3 3 5-7" fill="none" stroke="var(--check)" stroke-width="1.8"/></svg></td><td><svg viewBox="0 0 10 10"><path d="M2 2l6 6M8 2l-6 6" stroke="var(--cross)" stroke-width="2.2"/></svg></td></tr>
      <tr><td class="label">• Simple One Page Application</td><td><svg viewBox="0 0 10 10"><path d="M1 5l3 3 5-7" fill="none" stroke="var(--check)" stroke-width="1.8"/></svg></td><td><svg viewBox="0 0 10 10"><path d="M2 2l6 6M8 2l-6 6" stroke="var(--cross)" stroke-width="2.2"/></svg></td></tr>
      <tr><td class="label">• No Interest Rate (Flat Fee)</td><td><svg viewBox="0 0 10 10"><path d="M1 5l3 3 5-7" fill="none" stroke="var(--check)" stroke-width="1.8"/></svg></td><td><svg viewBox="0 0 10 10"><path d="M2 2l6 6M8 2l-6 6" stroke="var(--cross)" stroke-width="2.2"/></svg></td></tr>
      <tr><td class="label">• Bankruptcy OK</td><td><svg viewBox="0 0 10 10"><path d="M1 5l3 3 5-7" fill="none" stroke="var(--check)" stroke-width="1.8"/></svg></td><td><svg viewBox="0 0 10 10"><path d="M2 2l6 6M8 2l-6 6" stroke="var(--cross)" stroke-width="2.2"/></svg></td></tr>
      <tr><td class="label">• Opportunity to renew your cash<br>&nbsp;&nbsp;advance for additional funds</td><td><svg viewBox="0 0 10 10"><path d="M1 5l3 3 5-7" fill="none" stroke="var(--check)" stroke-width="1.8"/></svg></td><td><svg viewBox="0 0 10 10"><path d="M2 2l6 6M8 2l-6 6" stroke="var(--cross)" stroke-width="2.2"/></svg></td></tr>
    </table>
  </section>

  <p class="contact company">Blue Harbor Merchant Services</p>
  <p class="contact phone">555-014-2287</p>
  <p class="contact email">info@BlueHarborPay.com</p>

  <div class="footer-band"></div>
</main>
</body>
</html>
```